Harrowby Lending Hard Money Lender

We are looking for this flyer to be redesigned. We would like it to be even more simple than the attached design. No photos, no exclamation points, a 3-4 color palate maximum. We would do not want any graphics around the "Harrowby Lending" logo.

```html
<!DOCTYPE html>
<html lang="en">
<head>
<meta charset="utf-8">
<title>Harrowby Lending – Hard Money Loans</title>
<link rel="stylesheet" href="https://fonts.googleapis.com/css2?family=Anton&family=Questrial&display=swap">
<style>
  :root {
    --navy: #1b3049;
    --panel-top: #1c344d;
    --panel-bottom: #507fa0;
    --paper: #eeeeee;
    --orange: #f7941d;
    --white: #ffffff;
    --backdrop: #d9d9d9;
  }
  html, body {
    margin: 0;
    padding: 0;
    width: 952px;
    height: 1200px;
    overflow: hidden;
    background: var(--backdrop);
  }
  .flyer {
    position: absolute;
    left: 57px;
    top: 0;
    width: 837px;
    height: 1200px;
    background: var(--paper);
    overflow: hidden;
    font-family: "Anton", "Impact", sans-serif;
  }
  .side-panel {
    position: absolute;
    left: 0;
    top: 61px;
    width: 426px;
    height: 1139px;
    background: linear-gradient(to bottom, var(--panel-top), var(--panel-bottom));
    border-top-right-radius: 140px;
  }
  .brand-name {
    position: absolute;
    left: 19px;
    top: 331px;
    margin: 0;
    font-size: 54px;
    line-height: 54px;
    font-weight: 400;
    color: var(--white);
    white-space: nowrap;
  }
  .service-list {
    position: absolute;
    left: 76px;
    top: 510px;
    margin: 0;
    padding: 0;
    list-style: none;
  }
  .service-list li {
    display: flex;
    align-items: center;
    height: 62px;
    color: var(--white);
    font-size: 24.5px;
    line-height: 24.5px;
    letter-spacing: 2.6px;
    white-space: nowrap;
  }
  .service-list svg {
    width: 23px;
    height: 23px;
    margin-right: 14px;
    flex: none;
  }
  .phone-pill {
    position: absolute;
    left: 17px;
    top: 819px;
    width: 409px;
    height: 79px;
    background: var(--paper);
    border-radius: 40px 0 0 40px;
    display: flex;
    align-items: center;
  }
  .phone-number {
    margin-left: 52px;
    color: var(--orange);
    font-size: 60px;
    line-height: 60px;
    letter-spacing: 1px;
    white-space: nowrap;
  }
  .headline {
    position: absolute;
    left: 375px;
    top: 146px;
    width: 540px;
    margin: 0;
    font-weight: 400;
    color: var(--navy);
    text-align: center;
  }
  .headline span {
    display: block;
    height: 142px;
    font-size: 100px;
    line-height: 100px;
    white-space: nowrap;
    transform: scaleX(0.72);
    transform-origin: center top;
  }
  .headline .hard { letter-spacing: 0.33em; text-indent: 0.33em; }
  .headline .money { letter-spacing: 0.09em; text-indent: 0.09em; }
  .headline .loans { letter-spacing: 0.49em; text-indent: 0.49em; }
  .rate {
    position: absolute;
    left: 455px;
    top: 564px;
    width: 380px;
    margin: 0;
    text-align: center;
    color: var(--navy);
    font-size: 34px;
    line-height: 34px;
    letter-spacing: 2.5px;
  }
  .benefits {
    position: absolute;
    left: 453px;
    top: 0;
    width: 380px;
    color: var(--navy);
    text-align: center;
    letter-spacing: 2px;
  }
  .benefits p {
    position: absolute;
    left: 0;
    width: 100%;
    margin: 0;
    white-space: nowrap;
  }
  .benefits .benefit { font-size: 26.5px; line-height: 26.5px; }
  .benefits .approval { top: 680px; }
  .benefits .fees-1 { top: 726px; }
  .benefits .fees-2 { top: 752px; }
  .benefits .financing { top: 797px; }
  .benefits .note { top: 830px; font-size: 17px; line-height: 17px; letter-spacing: 1.6px; }
  .contact {
    position: absolute;
    left: 452px;
    top: 998px;
    font-family: "Questrial", "Century Gothic", sans-serif;
    color: var(--navy);
    font-size: 20.5px;
    line-height: 27.5px;
    letter-spacing: 2.3px;
    font-style: normal;
    white-space: nowrap;
  }
  .contact span { display: block; }
</style>
</head>
<body>
  <main class="flyer">
    <section class="side-panel">
      <h2 class="brand-name">Harrowby Lending</h2>
      <ul class="service-list">
        <li><svg viewBox="0 0 24 24" aria-hidden="true"><rect x="2" y="4" width="17" height="17" rx="3" fill="none" stroke="#fff" stroke-width="2.4"/><path d="M6 12 l4 4 L22 3" fill="none" stroke="#fff" stroke-width="2.6" stroke-linecap="round" stroke-linejoin="round"/></svg>Fix &amp; Flip Loans</li>
        <li><svg viewBox="0 0 24 24" aria-hidden="true"><rect x="2" y="4" width="17" height="17" rx="3" fill="none" stroke="#fff" stroke-width="2.4"/><path d="M6 12 l4 4 L22 3" fill="none" stroke="#fff" stroke-width="2.6" stroke-linecap="round" stroke-linejoin="round"/></svg>Commercial Loans</li>
        <li><svg viewBox="0 0 24 24" aria-hidden="true"><rect x="2" y="4" width="17" height="17" rx="3" fill="none" stroke="#fff" stroke-width="2.4"/><path d="M6 12 l4 4 L22 3" fill="none" stroke="#fff" stroke-width="2.6" stroke-linecap="round" stroke-linejoin="round"/></svg>Hard Money Loans</li>
      </ul>
      <div class="phone-pill"><span class="phone-number">555.210.4800</span></div>
    </section>

    <h1 class="headline">
      <span class="hard">HARD</span>
      <span class="money">MONEY</span>
      <span class="loans">LOANS</span>
    </h1>

    <p class="rate">Rates from 8%</p>

    <div class="benefits">
      <p class="benefit approval">Same-Day Approval</p>
      <p class="benefit fees-1">No Processing, Appraisal,</p>
      <p class="benefit fees-2">or Extra Fees</p>
      <p class="benefit financing">100% Financing</p>
      <p class="note">(w/ Additional Collateral)</p>
    </div>

    <address class="contact">
      <span>hello@harrowbylending.com</span>
      <span>www.harrowbylending.com</span>
      <span>4410 Larkspur Ave., Suite 200</span>
      <span>Aurelia, CO 80412</span>
    </address>
  </main>
</body>
</html>
```